Marlowen

I'm looking for business cards with the logo I've attached. I don't have an specific idea in mind and open to anything. All the usual info will be involved. Name, position in company, nr, email, address

```html
<!DOCTYPE html>
<html lang="en">
<head>
<meta charset="utf-8">
<title>Marlowen Business Card</title>
<link href="https://fonts.googleapis.com/css2?family=Montserrat:wght@500;700&family=Arimo:wght@400;700&display=swap" rel="stylesheet">
<style>
  :root {
    --bg: #3a3a3c;
    --gold: #edb237;
    --gold-light: #f1c04a;
    --gold-deep: #dfa22a;
    --navy: #1b2a47;
    --paper: #ffffff;
    --rule: #d6d6d6;
  }
  * { box-sizing: border-box; margin: 0; padding: 0; }
  html, body {
    width: 1200px;
    height: 1015px;
    overflow: hidden;
    background: var(--bg);
  }
  .canvas {
    position: relative;
    width: 1200px;
    height: 1015px;
  }
  .card {
    position: absolute;
    left: 250px;
    width: 700px;
    height: 400px;
    overflow: hidden;
    box-shadow: 0 10px 24px rgba(0,0,0,0.45);
  }
  .card--back {
    top: 60px;
    background: var(--gold);
  }
  .back-pattern {
    position: absolute;
    inset: 0;
    background:
      repeating-linear-gradient(-35deg,
        rgba(241,192,74,0) 0px,
        rgba(241,192,74,0.55) 22px,
        rgba(241,192,74,0) 44px,
        rgba(223,162,42,0.35) 66px,
        rgba(241,192,74,0) 88px),
      linear-gradient(135deg, var(--gold-light) 0%, var(--gold) 55%, var(--gold-deep) 100%);
  }
  .back-brand {
    position: absolute;
    right: 64px;
    top: 50%;
    transform: translateY(-50%);
    font-family: "Montserrat", sans-serif;
    font-weight: 700;
    font-size: 26px;
    letter-spacing: 1px;
    color: var(--paper);
  }
  .card--front {
    top: 555px;
    background: var(--paper);
  }
  .divider {
    position: absolute;
    inset: 0;
  }
  .brand {
    position: absolute;
    left: 48px;
    top: 178px;
    display: flex;
    align-items: center;
    gap: 12px;
  }
  .brand-dot {
    width: 26px;
    height: 26px;
    border-radius: 50%;
    background: var(--navy);
  }
  .brand-name {
    font-family: "Montserrat", sans-serif;
    font-weight: 700;
    font-size: 34px;
    letter-spacing: 1px;
    color: var(--gold);
    line-height: 1;
  }
  .details {
    position: absolute;
    left: 415px;
    top: 92px;
    font-family: "Arimo", sans-serif;
    color: var(--navy);
  }
  .person-name {
    font-family: "Montserrat", sans-serif;
    font-weight: 700;
    font-size: 25px;
    color: var(--gold);
    line-height: 1;
  }
  .person-role {
    font-size: 17px;
    margin-top: 4px;
  }
  .contact-list {
    list-style: none;
    margin-top: 22px;
  }
  .contact-list li {
    display: flex;
    align-items: center;
    gap: 9px;
    font-size: 17px;
    line-height: 26px;
  }
  .contact-list svg {
    width: 16px;
    height: 16px;
    flex: none;
  }
  .accent { color: var(--gold); }
  .address {
    margin-top: 16px;
    font-size: 17px;
    line-height: 23px;
    padding-left: 25px;
  }
</style>
</head>
<body>
<main class="canvas">
  <section class="card card--back">
    <div class="back-pattern" role="img" aria-label="Repeating diagonal brand wordmark pattern in tonal gold"></div>
    <div class="back-brand">MARLOWEN</div>
  </section>

  <section class="card card--front">
    <svg class="divider" viewBox="0 0 700 400" aria-hidden="true">
      <line x1="345" y1="0" x2="405" y2="400" stroke="var(--rule)" stroke-width="1.2"/>
    </svg>

    <div class="brand">
      <span class="brand-dot"></span>
      <span class="brand-name">MARLOWEN</span>
    </div>

    <div class="details">
      <h1 class="person-name">DANIEL ASHFORD</h1>
      <p class="person-role">Managing Director</p>
      <ul class="contact-list">
        <li>
          <svg viewBox="0 0 16 16" aria-hidden="true"><path fill="var(--gold)" d="M3.6 1.5l2.2 2.6-1.3 1.6c.9 2 2.5 3.6 4.5 4.6l1.6-1.3 2.6 2.2-1.2 2.2C7 12.9 3 8.9 1.6 3l2-1.5z"/></svg>
          044-555 210 347
        </li>
        <li>
          <svg viewBox="0 0 16 16" aria-hidden="true"><rect x="1" y="3.5" width="14" height="9" fill="var(--gold)"/><path d="M1 3.5l7 5.5 7-5.5" fill="none" stroke="#fff" stroke-width="1.2"/></svg>
          info@marlowen.com
        </li>
        <li>
          <svg viewBox="0 0 16 16" aria-hidden="true"><circle cx="8" cy="8" r="6.5" fill="none" stroke="var(--gold)" stroke-width="1.6"/><ellipse cx="8" cy="8" rx="2.8" ry="6.5" fill="none" stroke="var(--gold)" stroke-width="1.2"/><line x1="1.5" y1="8" x2="14.5" y2="8" stroke="var(--gold)" stroke-width="1.2"/></svg>
          <span>www.<span class="accent">marlowenstudio</span>.com</span>
        </li>
      </ul>
      <p class="address">87, Harbor Crest Lane<br>31208, Westmere</p>
    </div>
  </section>
</main>
</body>
</html>
```